Brivtel sales folder inserts

We need the same design for 4 separate service offerings to put inside our sales folder. Each insert should be laid out the same with different images and text and the 2nd, 3rd, and 4th should each be 3/4" shorter than the previous one so that when all 4 are inserted into the folder you see the black strip with text showing what the service offering is. Basically staggered inserts.

Industry/Entity Type

Information Technology

Font styles to use
Sans Serif

Colors
acd136

Requirements
Must have
• Brivtel logo and included text. Keep with the green Pantone 90 and black color scheme
Nice to have
• a better layout and pics

```html
<!DOCTYPE html>
<html lang="en">
<head>
<meta charset="utf-8">
<title>Brivtel sales folder inserts</title>
<link href="https://fonts.googleapis.com/css2?family=Roboto:wght@400;500;700&family=Roboto+Condensed:wght@400;700&display=swap" rel="stylesheet">
<style>
:root{
  --green:#acd136;
  --green-text:#8fb51f;
  --black:#141414;
  --dark:#222;
  --panel-dark:#1c1c1c;
  --white:#fff;
  --ink:#2a2a2a;
  --stage:#e6e6e4;
}
*{box-sizing:border-box;margin:0;padding:0}
html,body{width:1200px;height:429px;overflow:hidden;background:var(--stage);font-family:"Roboto",sans-serif}
.stage{position:relative;width:1200px;height:429px}
.insert{position:absolute;width:250px;background:var(--white);overflow:hidden;box-shadow:0 2px 6px rgba(0,0,0,.25)}
.insert--business{left:49px;top:51px;height:324px}
.insert--it{left:326px;top:73px;height:302px}
.insert--secure{left:602px;top:95px;height:280px}
.insert--voice{left:882px;top:118px;height:257px}

.strip{position:relative;height:22px;background:linear-gradient(#2a2a2a,var(--black));color:var(--white);display:flex;align-items:center}
.strip__title{font-weight:500;font-size:5.4px;padding-left:16px;letter-spacing:.1px}
.strip__tab{position:absolute;right:0;top:4px;height:14px;width:82px;background:var(--green);clip-path:polygon(10% 0,100% 0,100% 100%,0 100%);color:var(--white);font-weight:700;font-size:7px;display:flex;align-items:center;justify-content:flex-end;padding-right:6px}

.photo{height:var(--photo-h,93px)}
.photo--business{background:linear-gradient(120deg,#3e4a55,#9fb0bd 45%,#55606a)}
.photo--it{background:linear-gradient(120deg,#4d6c66,#a5c4bd 40%,#2f3e3d)}
.photo--secure{background:linear-gradient(120deg,#1f4459,#6fa3bd 45%,#173244)}
.photo--voice{background:linear-gradient(120deg,#5a3a2e,#8aa6c0 45%,#3d5a78)}

.body{position:absolute;left:0;right:0;bottom:0;top:calc(22px + var(--photo-h,93px));display:flex}
.col-info{width:131px;padding:7px 8px 0 12px;color:var(--ink);font-size:3.3px;line-height:1.35}
.col-detail{position:relative;width:119px;background:linear-gradient(var(--dark),var(--panel-dark));color:var(--white);font-size:3.2px;line-height:1.35;padding:40px 6px 0 0}
.dark-rise{position:absolute;right:0;width:119px;height:44px;background:var(--dark);clip-path:polygon(0 60%,100% 0,100% 100%,0 100%);top:calc(22px + var(--photo-h,93px) - 44px)}
.device{position:absolute;right:14px;width:84px;height:48px;top:calc(22px + var(--photo-h,93px) - 40px);background:linear-gradient(#cfd4d8,#8c939a);border:2px solid #333;border-radius:2px}

.brand{display:flex;align-items:center;gap:6px;margin-bottom:10px}
.brand__square{width:14px;height:14px;background:var(--green)}
.brand__name{font-weight:700;font-size:10px;color:var(--ink);letter-spacing:.6px}
.col-info h2{font-family:"Roboto Condensed",sans-serif;font-weight:400;font-size:5.8px;color:var(--green-text);margin-bottom:3px}
.lead{font-weight:700}
.col-info p{margin-bottom:3px}
.col-info ul{list-style:none}
.col-info li{position:relative;padding-left:6px;margin-bottom:3px}
.col-info li::before{content:"";position:absolute;left:0;top:1px;width:1.6px;height:1.6px;background:var(--green)}

.label{display:inline-block;background:var(--green);color:var(--black);font-size:4.2px;padding:1.5px 14px 1.5px 5px;clip-path:polygon(0 0,92% 0,100% 100%,0 100%);margin:2px 0 3px}
.col-detail ul{list-style:none;padding-left:6px;margin-bottom:2px}
.col-detail li{position:relative;padding-left:5px;margin-bottom:2.5px}
.col-detail li::before{content:"";position:absolute;left:0;top:.8px;width:2px;height:2px;border-radius:50%;background:var(--green)}
.ticks li::before{content:"\2713";background:none;color:var(--green);font-size:3px;top:0;width:auto;height:auto}
.stats{padding-left:6px}
.stats p{margin-bottom:3px}
.stats b{color:var(--green);font-weight:400;font-size:4.4px}
.adv{padding-left:6px}
.adv p{margin-bottom:2.5px}
.adv em{display:block;font-style:normal;color:var(--green)}
.closing{position:absolute;bottom:5px;left:0;right:0;text-align:center;font-family:"Roboto Condensed",sans-serif;font-weight:700;color:var(--green);font-size:4.6px;letter-spacing:.2px}
</style>
</head>
<body>
<main class="stage">

<section class="insert insert--business" style="--photo-h:93px">
  <header class="strip"><span class="strip__title">PRO-BUSINESS RUN ANYWHERE, PROTECT ANYTHING</span><span class="strip__tab">PRO-BUSINESS</span></header>
  <div class="photo photo--business" role="img" aria-label="Business continuity photo: hand touching cloud and device icons over a world map"></div>
  <div class="body">
    <div class="col-info">
      <div class="brand"><span class="brand__square"></span><span class="brand__name">BRIVTEL</span></div>
      <h2>RUN ANYWHERE, PROTECT ANYTHING</h2>
      <p><span class="lead">Your Business Continuity Solution.</span><br>Brivtel's PRO-BUSINESS solution provides comprehensive backups for your data like never before.</p>
      <ul>
        <li>In todays environment threats are never ending. There is always a new threat trying to get to your data, whether to Kryvault lock it and hold it for ransom, or be malicious and delete it for no reason at all.</li>
        <li>Keeping your network up to date and monitoring for suspicious activity are all recommended actions, but backing up your data is the most important action you can take.</li>
        <li>Don't just back up your data. Verify it. What good is a backup of your data if it does not work when you need it. The Brivtel PRO-Business solution tests and verifies your data on a daily basis.</li>
        <li>The PRO-Business solution also provides you a local and an off-site copy of your data. What good is a business continuity plan if your backups burn down with your building.</li>
        <li>The PRO-Business solution provides an onsite server resource should you need it, as well as allowing you to spin up virtual servers in the cloud during a disaster scenario.</li>
      </ul>
    </div>
    <div class="col-detail">
      <span class="label">Does your backup solution do this?</span>
      <ul>
        <li>Test and verify your backups by booting on a virtual server in the cloud</li>
        <li>Backup your CloudDesk Suite</li>
        <li>Allow you to spin up virtual servers in the cloud during a disaster</li>
      </ul>
      <span class="label">Did You Know?</span>
      <div class="stats">
        <p><b>60%</b> of backups are incomplete</p>
        <p><b>50%</b> of restores fail</p>
        <p><b>40%</b> of the SMB market will be attacked by a hacker, 50% wont even know it.</p>
        <p><b>20%</b> of SMB market will lose critical data every 5-years</p>
        <p><b>90%</b> of business that lost data for 10-days or more filed for bankruptcy immediately</p>
      </div>
      <p class="closing">A LITTLE MISTAKE CAN COST A FORTUNE</p>
    </div>
  </div>
  <div class="dark-rise"></div>
  <div class="device" role="img" aria-label="Laptop showing a green padlock on a data screen"></div>
</section>

<section class="insert insert--it" style="--photo-h:92px">
  <header class="strip"><span class="strip__title">PRO-IT PROACTIVE IT SUPPORT</span><span class="strip__tab">PRO-IT</span></header>
  <div class="photo photo--it" role="img" aria-label="IT support photo: businessman touching holographic screens over a city"></div>
  <div class="body">
    <div class="col-info">
      <div class="brand"><span class="brand__square"></span><span class="brand__name">BRIVTEL</span></div>
      <h2>A TRUE IT PARTNERSHIP</h2>
      <p><span class="lead">An IT partner not provider.</span><br>We understand why your critical business services are so important to your daily operations. This is why we spend so much time aligning our technology support with just such business services. Our program couples 24x7x365 network monitoring with an aggressive preventative maintenance component to ensure optimum uptime for your business.</p>
      <ul>
        <li>One of the major challenges in maintaining a computer network is trying to predict what will fail and when. With our PRO-IT solution, we can prevent many network failures from ever happening. By combining regular and comprehensive preventative maintenance and robust real-time monitoring of your critical network and desktop devices, we ensure the reliability and stability of your IT assets.</li>
        <li>This solution is so effective, our customers see almost immediate results. A regularly maintained network means fewer failures, higher productivity and savings on support costs for you. Exposure to security risks is dramatically lessened, and frustration from unstable IT resources almost vanishes.</li>
      </ul>
    </div>
    <div class="col-detail">
      <span class="label">Do these issues plague your business?</span>
      <ul>
        <li>Network neglected? Is yours perceived as a "necessary evil" and not as integral to improving business performance?</li>
        <li>Downtime impact? Are IT outages distracting your staff from their core focus?</li>
        <li>Distracted employees? Do your staff rely on other non-IT employees to deal with IT problems?</li>
      </ul>
      <span class="label">Program Advantages:</span>
      <div class="adv">
        <p><em>Increased productivity:</em>Continuous insight into your network lets us reduce the business impact of IT failure by shortening resolution time.</p>
        <p><em>Reduced business impact from IT failures:</em>Maintenance and remote monitoring mean we minimize failures that could impact your business.</p>
        <p><em>Reduced network downtime through proactive maintenance:</em>Regular preventative activities keep your network efficient and reduce emergency incidents.</p>
      </div>
      <p class="closing">Stop Buying Downtime &ndash; Invest in Uptime</p>
    </div>
  </div>
  <div class="dark-rise"></div>
  <div class="device" role="img" aria-label="Laptop showing a network monitoring dashboard"></div>
</section>

<section class="insert insert--secure" style="--photo-h:92px">
  <header class="strip"><span class="strip__title">PRO-SECURE &nbsp;- SECURE YOUR ASSETS</span><span class="strip__tab">PRO-SECURE</span></header>
  <div class="photo photo--secure" role="img" aria-label="Security photo: person using a tablet with blue data overlays"></div>
  <div class="body">
    <div class="col-info">
      <div class="brand"><span class="brand__square"></span><span class="brand__name">BRIVTEL</span></div>
      <h2>PRO-SECURE SECURITY AT ITS BEST</h2>
      <p><span class="lead">PRO-SECURE provides piece of mind.</span><br>Secure your company with industry leading cameras and door access systems. Monitor your business like you monitor your accounts.</p>
      <ul>
        <li>Brivtel provides network video recorders and IP-CCTV cameras with intelligence. Keeping an eye on your business 24X7 is essential in todays environment.</li>
        <li>Having the ability to go back in time and review what happened is becoming more important by the day. A video of an incident can mean the difference between settling out of court or dismissing the case entirely.</li>
        <li>Securing your entry points to your site is crucial. With a card access system from Brivtel you will have control of who has access and when. Never have to worry about lost keys.</li>
      </ul>
    </div>
    <div class="col-detail">
      <span class="label">Do I need these types of systems?</span>
      <ul>
        <li>I use hard keys? Hard keys can be lost, copied, and not returned. Card access gives you control.</li>
        <li>I trust my people, I don't need video cameras? This is not a matter of trust, it is a matter of security.</li>
        <li>This sounds complicated? Brivtel can provide complete management of these systems. A single call gets it all done.</li>
      </ul>
      <span class="label">What Can I Do With These Systems?</span>
      <ul class="ticks">
        <li>Receive alerts according to events</li>
        <li>Review events of the past</li>
        <li>Increase security with access events</li>
        <li>Enhanced reporting capabilities</li>
        <li>View video from anywhere</li>
        <li>End lost or copied keys</li>
        <li>Provide employees piece of mind</li>
        <li>24X7 On Call Services</li>
      </ul>
      <p class="closing">SECURE YOUR ASSETS</p>
    </div>
  </div>
  <div class="dark-rise"></div>
  <div class="device" role="img" aria-label="Laptop showing security cameras, radio and keypad"></div>
</section>

<section class="insert insert--voice" style="--photo-h:87px">
  <header class="strip"><span class="strip__title">PRO-SECURE - SECURE YOUR ASSETS</span><span class="strip__tab">PRO-VOICE</span></header>
  <div class="photo photo--voice" role="img" aria-label="Voice services photo: business handshake with light trails"></div>
  <div class="body">
    <div class="col-info">
      <div class="brand"><span class="brand__square"></span><span class="brand__name">BRIVTEL</span></div>
      <h2>PRO-VOICE, EVERY OPTION</h2>
      <p><span class="lead">PRO-VOICE provides endless options.</span><br>Working with Brivtel provides you with options. We work with every provider so you can select the best option for your needs.</p>
      <ul>
        <li>Brivtel offers both On-Premise Unified Communication solutions and Hosted Unified Communication solutions.</li>
        <li>No matter what your need is Brivtel has the solution with our PRO-Voice program.</li>
        <li>Brivtel has relationships with almost every provider for internet and voice connections for your business.</li>
        <li>We can provide quotes from any provider in the area.</li>
        <li>More options can mean larger savings. You will have the information to make the best selection for your business needs.</li>
      </ul>
    </div>
    <div class="col-detail">
      <span class="label">How can Brivtel assist?</span>
      <ul>
        <li>Provide multiple options for review</li>
        <li>Provide cost savings</li>
        <li>Educate client on options</li>
        <li>Locate possible cost over runs on existing provider solutions</li>
        <li>Provide turn key solutions</li>
        <li>Provide On-Premise Solutions</li>
        <li>Provide Hosted Solutions</li>
        <li>Multi-site and remote worker solutions</li>
        <li>Contact center solutions</li>
        <li>Multi media Contact Center Solutions</li>
        <li>Advance Reporting and Monitoring</li>
      </ul>
      <p class="closing">GIVE YOURSELF OPTIONS, AND WE CAN HELP YOU<br>CHOOSE THE RIGHT OPTION</p>
    </div>
  </div>
  <div class="dark-rise"></div>
  <div class="device" role="img" aria-label="Laptop showing cloud and communication device icons"></div>
</section>

</main>
</body>
</html>
```